Hacienda Las Verbenas Website

I need a template design for Hacienda Las Verbenas which is a Residential and Commercial development project to be located in Panama.

The look of the website has to be "country" since it is a Hacienda. It has to take in the feel of being out with nature.

The Logo of the project is contained in the attached files as well as pictures of the Project´s conceptual design and several air pictures of the land where the project will be built.

Industry/Entity Type

Residential

Requirements
Must have
• The website has to be very simple, very visual, a lot of images. The Main Menu has to be:
1. Home
2. About us
3. The project
4. Location
5. Contact us

```html
<!DOCTYPE html>
<html lang="en">
<head>
<meta charset="utf-8">
<title>Hacienda Las Verbenas</title>
<link href="https://fonts.googleapis.com/css2?family=PT+Sans:ital,wght@0,400;0,700;1,400&display=swap" rel="stylesheet">
<style>
:root{
  --ink:#333333;
  --heading:#4f4f51;
  --gold:#8a5a1a;
  --nav:#4c4c4e;
  --button:#5a5a5c;
  --footer:#6b6b6d;
  --bubble:#ececec;
  --muted:#777777;
  --white:#ffffff;
}
*{margin:0;padding:0;box-sizing:border-box}
html,body{width:1124px;height:1200px;overflow:hidden;background:var(--white)}
body{position:relative;font-family:"PT Sans",sans-serif;color:var(--ink)}
.abs{position:absolute}

.brand{left:169px;top:30px;display:flex;align-items:center;gap:10px}
.brand-mark{width:30px;height:30px;background:var(--gold)}
.brand-name{font-size:27px;font-weight:700;color:var(--gold);line-height:1}

.follow{left:645px;top:66px;font-size:9px;color:var(--muted)}
.social{top:58px;width:26px;height:26px;border-radius:50%}
.call{left:872px;top:53px;font-size:9px;color:var(--ink)}
.call strong{display:block;font-size:12px;color:var(--gold);font-weight:400;letter-spacing:1px;margin-top:2px}

.nav{left:169px;top:111px;width:787px;height:34px;background:var(--nav)}
.nav a{position:absolute;top:11px;font-size:9.5px;font-weight:700;color:var(--white);text-decoration:none}
.search{position:absolute;left:587px;top:6px;width:191px;height:20px;background:#f2f2f2;border-radius:2px;font-size:9px;color:#888;padding:5px 10px}

.hero{left:0;top:145px;width:1124px;height:375px;background:linear-gradient(180deg,#6f8a5c 0%,#4e6e3a 45%,#5a7440 75%,#7a7f5a 100%)}
.hero-arrow{position:absolute;top:303px}
.hero-title{left:169px;top:355px;font-size:22px;font-weight:700;color:var(--white);line-height:32px}

.welcome{left:0;top:543px;width:1124px;text-align:center;font-size:21px;font-weight:700;color:var(--heading)}
.intro{left:180px;top:580px;width:764px;text-align:center;font-size:9.4px;line-height:16px}
.section-title{font-size:14px;font-weight:700;color:var(--heading)}

.service{top:671px;width:244px}
.service .photo{height:106px}
.service h3{font-size:12.5px;font-weight:700;color:var(--heading);margin:12px 0 6px 1px}
.service p{font-size:9.2px;line-height:16px;margin-left:1px}
.btn{display:inline-block;margin-top:12px;width:84px;height:23px;background:var(--button);border-radius:2px;color:var(--white);font-size:9.5px;text-align:center;line-height:23px}

.pager{top:934px;display:flex;gap:3px}
.pager span{width:12px;height:12px;background:#cfcfcf;display:block}

.project{top:962px;width:152px}
.project .photo{height:90px;border:2px solid #e5e5e5}
.project h4{font-size:9.4px;font-weight:700;color:var(--gold);margin-top:10px}
.project p{font-size:9.2px;font-style:italic;line-height:16px;margin-top:4px}

.bubble{left:696px;top:965px;width:260px;height:87px;background:var(--bubble);padding:19px 18px 0 24px;font-size:9.2px;font-style:italic;line-height:16px}
.avatar{left:698px;top:1071px;width:48px;height:48px;background:linear-gradient(#cfd6dc,#a7b2ba)}
.author{left:758px;top:1074px;font-size:8.6px;font-weight:700;color:var(--gold)}
.posted{left:758px;top:1090px;font-size:8.4px;font-style:italic;color:var(--muted)}

.footer{left:0;top:1148px;width:1124px;height:52px;background:var(--footer)}
.footer-links{position:absolute;left:170px;top:19px;font-size:8px;color:var(--white);display:flex;gap:14px}
.copyright{position:absolute;right:169px;top:19px;font-size:7.6px;color:var(--white)}
</style>
</head>
<body>

<div class="abs brand"><span class="brand-mark"></span><span class="brand-name">Hacienda Las Verbenas</span></div>

<div class="abs follow">FOLLOW US :</div>
<span class="abs social" style="left:704px;background:#2a64b0"></span>
<span class="abs social" style="left:733px;background:#3aa6dd"></span>
<span class="abs social" style="left:762px;background:#1f6e9a"></span>
<span class="abs social" style="left:791px;background:#333"></span>

<svg class="abs" style="left:837px;top:50px" width="22" height="36" viewBox="0 0 22 36" aria-hidden="true">
  <rect x="1" y="1" width="20" height="34" rx="3" fill="#2b2b2b"/>
  <rect x="4" y="5" width="14" height="23" fill="#2f8fd8"/>
  <circle cx="11" cy="31" r="1.6" fill="#777"/>
</svg>
<div class="abs call">CALL US :<strong>( 5550 ) 248 913</strong></div>

<nav class="abs nav">
  <a style="left:30px">HOME</a>
  <a style="left:118px">ABOUT US</a>
  <a style="left:221px">THE PROJECT</a>
  <a style="left:337px">LOCATION</a>
  <a style="left:440px">CONTACT US</a>
  <div class="search">Search :</div>
</nav>

<section class="abs hero" role="img" aria-label="Aerial photograph of green hills with a winding highway through the project land">
</section>
<svg class="abs hero-arrow" style="left:83px;top:303px" width="60" height="60" viewBox="0 0 60 60" aria-hidden="true">
  <circle cx="30" cy="30" r="28" fill="none" stroke="rgba(255,255,255,.45)" stroke-width="2"/>
  <path d="M38 20 L20 30 L38 40 Z" fill="rgba(255,255,255,.45)"/>
</svg>
<svg class="abs hero-arrow" style="left:974px;top:303px" width="60" height="60" viewBox="0 0 60 60" aria-hidden="true">
  <circle cx="30" cy="30" r="28" fill="none" stroke="rgba(255,255,255,.45)" stroke-width="2"/>
  <path d="M22 20 L40 30 L22 40 Z" fill="rgba(255,255,255,.45)"/>
</svg>
<h1 class="abs hero-title">RESIDENTIAL AND<br>COMMERCIAL DEVELOPMENT PROJECT IN PANAMA</h1>

<h2 class="abs welcome">WELCOME TO LAS VERBENAS</h2>
<p class="abs intro">Lorem Ipsum is simply dummy text of the printing and typesetting industry. Lorem Ipsum has been the industry's standard dummy text ever since the 1500s, when an unknown printer took a galley of type and scrambled it to make a type specimen book. It has survived not only five centuries, but also the leap into electronic typesetting.</p>

<h2 class="abs section-title" style="left:0;width:1124px;text-align:center;top:633px">SERVICES</h2>

<article class="abs service" style="left:169px">
  <div class="photo" role="img" aria-label="Rendering of a modern commercial building" style="background:linear-gradient(180deg,#8fb0d6,#9a9a92 70%,#6e6e68)"></div>
  <h3>Commercial development</h3>
  <p>Lorem Ipsum is simply dummy text of the printing and typesetting industry. Lorem Ipsum has been the industry's standard dummy text ever since the 1500s...</p>
  <span class="btn">READ MORE</span>
</article>
<article class="abs service" style="left:441px">
  <div class="photo" role="img" aria-label="Aerial photograph of green forested land" style="background:linear-gradient(180deg,#5f7f44,#4a6a34 60%,#7a7a4c)"></div>
  <h3>Commercial development</h3>
  <p>Lorem Ipsum is simply dummy text of the printing and typesetting industry. Lorem Ipsum has been the industry's standard dummy text ever since the 1500s...</p>
  <span class="btn">READ MORE</span>
</article>
<article class="abs service" style="left:712px">
  <div class="photo" role="img" aria-label="Rendering of high-rise towers" style="background:linear-gradient(180deg,#c8d4e0,#8d9aa6 60%,#4a4e54)"></div>
  <h3>Commercial development</h3>
  <p>Lorem Ipsum is simply dummy text of the printing and typesetting industry. Lorem Ipsum has been the industry's standard dummy text ever since the 1500s...</p>
  <span class="btn">READ MORE</span>
</article>

<h2 class="abs section-title" style="left:169px;top:931px">PROJECTS</h2>
<div class="abs pager" style="left:630px"><span></span><span></span></div>

<article class="abs project" style="left:169px">
  <div class="photo" role="img" aria-label="Rendering of a landscaped roundabout" style="background:linear-gradient(180deg,#4f7a3c,#9a9a98 50%,#3f6a30)"></div>
  <h4>COMMERCIAL DEVELOPMENT</h4>
  <p>Lorem Ipsum is simply dummy text of the printing...</p>
</article>
<article class="abs project" style="left:338px">
  <div class="photo" role="img" aria-label="Rendering of an entrance road lined with trees" style="background:linear-gradient(180deg,#6f93c4,#4f7a3c 45%,#8a8a8a)"></div>
  <h4>COMMERCIAL DEVELOPMENT</h4>
  <p>Lorem Ipsum is simply dummy text of the printing...</p>
</article>
<article class="abs project" style="left:507px">
  <div class="photo" role="img" aria-label="Rendering of a brick gateway under blue sky" style="background:linear-gradient(180deg,#7aa6dc,#b06a44 55%,#5f7a48)"></div>
  <h4>COMMERCIAL DEVELOPMENT</h4>
  <p>Lorem Ipsum is simply dummy text of the printing...</p>
</article>

<h2 class="abs section-title" style="left:699px;top:931px">TESTIMONIALS</h2>
<div class="abs pager" style="left:927px"><span></span><span></span></div>

<div class="abs bubble">Lorem Ipsum is simply dummy text of the printing and typesetting industry. Lorem Ipsum has been the industry's standard dummy text ever since the 1500s...</div>
<svg class="abs" style="left:855px;top:1051px" width="48" height="28" viewBox="0 0 48 28" aria-hidden="true">
  <path d="M4 0 L48 0 L0 28 Z" fill="var(--bubble)"/>
</svg>
<div class="abs avatar" role="img" aria-label="Portrait of the reviewer"></div>
<div class="abs author">MARCUS ELLERY</div>
<div class="abs posted">Posted on 20 Jul 2013</div>

<footer class="abs footer">
  <div class="footer-links"><span>HOME</span><span>|</span><span>ABOUT US</span><span>|</span><span>THE PROJECT</span><span>|</span><span>LOCATION</span><span>|</span><span>CONTACT US</span></div>
  <div class="copyright">© COPYRIGHT 2013. LAS VERBENAS. ALL RIGHTS RESERVED.</div>
</footer>

</body>
</html>
```